Ferrowave.com website design

I need a basic website for www.ferrowave.com. Ferro Wave has been hosting websites since 2002 via partnership arrangement with Stackhollow.com and Namequarry.com. We do not do any design, only hosting for small companies and nonprofits. We are referring people to PixelGuild and others to get their websites developed. Our website and pricing does not change often, but I need to be able to easily update the pricing and contact page.

Target Market(s)

Small company and non profit organizations

Industry/Entity Type

Utility

Coding

Coded - Design and coding required

Number of Pages Required

5+ page

Colors

Designer to choose colors to be used in the design.

Requirements
Must have
• Wordsmith format for easy content management. The logo attached. Contact us page with the following: Phone and fax are the same number: 888.514.2973. Email address is myferrowave@mailnest.example. Mailing address is 4819 E. Tolliver Bend #317, Searcy, AR 72143.
Nice to have
• Some kind of badge or tag line on the home page that celebrates our 15th year of hosting without a single hosting without any downtime. We are are 15 year partners with Stackhollow.com and Namequarry.com. Website Design tab needs to reference PixelGuild or others for all their website design needs. We provide no design or updating services. We will provide the developers FTP access to our dedicated Linux server. We do not provide email services other than redirects to their proprietary email or gmail, yahoo, etc. Needs a services and pricing tab. We provide domain registration services via our partnership with Namequarry.com. We will want a way for them to submit a suggested domain name for us to verify if available. I might be able to get a link from Namequarry.com to our account for you to include on that tab REGISTER DOMAIN. The tab buttons can be: WHO WE ARE, WHAT WE DO, WHEN YOU NEED US, WHERE TO REACH US. Maybe consider making the WHO, WHAT, WHEN and WHERE a dark blue color the rest of the text different color just so they stand out
Should not have
• A lot of animation that takes a long time to open. Clean and simple website.

```html
<!DOCTYPE html>
<html lang="en">
<head>
<meta charset="utf-8">
<title>Ferro Wave — Web Hosting</title>
<link href="https://fonts.googleapis.com/css2?family=Montserrat:wght@400;600;700;800&family=Lato:wght@400;700&display=swap" rel="stylesheet">
<style>
  :root {
    --blue: #2f86d6;
    --blue-dark: #1f5fa3;
    --navy: #1b2a3c;
    --ink: #2c3440;
    --muted: #7b8591;
    --hero-top: #2a3a50;
    --hero-bottom: #0f1826;
    --footer: #23272d;
    --footer-text: #a7adb5;
    --white: #ffffff;
    --rule: #e3e7ec;
  }
  * { box-sizing: border-box; margin: 0; padding: 0; }
  html, body { width: 1200px; height: 2192px; overflow: hidden; }
  body { font-family: "Lato", sans-serif; color: var(--ink); background: var(--white); }
  .heading { font-family: "Montserrat", sans-serif; }

  /* Header */
  .site-header { height: 88px; position: relative; background: var(--white); }
  .brand { position: absolute; left: 120px; top: 22px; display: flex; align-items: center; gap: 12px; }
  .brand-mark { width: 40px; height: 40px; background: var(--blue); }
  .brand-name { font-family: "Montserrat", sans-serif; font-weight: 800; font-size: 20px; color: var(--navy); letter-spacing: 1px; }
  .account-bar { position: absolute; right: 120px; top: 12px; display: flex; align-items: center; gap: 14px; font-family: "Montserrat", sans-serif; font-size: 10px; font-weight: 700; color: var(--navy); }
  .search { width: 150px; height: 22px; border: 1px solid var(--rule); font-size: 9px; color: var(--muted); padding: 5px 8px; font-weight: 400; display: flex; justify-content: space-between; }
  .main-nav { position: absolute; right: 120px; top: 54px; display: flex; gap: 28px; font-family: "Montserrat", sans-serif; font-size: 11px; font-weight: 700; }
  .main-nav .key { color: var(--blue-dark); }
  .main-nav .rest { color: var(--blue); }

  /* Hero */
  .hero { position: relative; height: 532px; background: linear-gradient(180deg, var(--hero-top), var(--hero-bottom)); }
  .hero-badge { position: absolute; left: 430px; top: 70px; }
  .scroll-cue { position: absolute; left: 589px; top: 482px; }

  /* Welcome */
  .welcome { height: 380px; text-align: center; padding-top: 62px; }
  .section-title { font-family: "Montserrat", sans-serif; font-weight: 800; font-size: 28px; color: var(--navy); letter-spacing: .5px; }
  .section-title .accent { color: var(--blue); }
  .welcome p { width: 880px; margin: 18px auto 0; font-size: 12px; line-height: 1.6; color: var(--muted); }
  .welcome-art { width: 300px; height: 170px; margin: 22px auto 0; border-radius: 8px; background: linear-gradient(135deg, #d8e9f8, #9cc7ec); }

  /* Services */
  .services { height: 455px; background: var(--blue); padding-top: 50px; text-align: center; }
  .services .section-title { color: var(--white); }
  .services .section-title .accent { color: var(--navy); }
  .title-rule { width: 70px; height: 3px; background: var(--white); margin: 10px auto 0; }
  .card-row { display: flex; justify-content: center; gap: 44px; margin-top: 30px; }
  .card { width: 260px; height: 310px; background: var(--white); border-radius: 4px; padding: 26px 26px 0; box-shadow: 0 6px 16px rgba(0,0,0,.15); }
  .card-art { width: 96px; height: 70px; margin: 0 auto; border-radius: 6px; background: linear-gradient(135deg, #cfe3f6, #8dbde8); }
  .card-title { font-family: "Montserrat", sans-serif; font-weight: 700; font-size: 12px; color: var(--blue); margin-top: 14px; line-height: 1.35; min-height: 32px; }
  .price { font-family: "Montserrat", sans-serif; font-size: 46px; color: #9aa3ad; font-weight: 400; margin-top: 4px; }
  .card p { font-size: 11px; color: var(--muted); line-height: 1.5; margin-top: 4px; }
  .button { display: inline-block; background: var(--navy); color: var(--white); font-family: "Montserrat", sans-serif; font-weight: 700; font-size: 9px; letter-spacing: .5px; padding: 9px 18px; margin-top: 14px; }

  /* Suggest domain */
  .suggest { height: 240px; background: linear-gradient(180deg, #3a414a, #2b3037); text-align: center; padding-top: 72px; color: var(--white); }
  .suggest .section-title { color: var(--white); }
  .suggest p { font-size: 12px; color: #c6ccd3; margin-top: 8px; }
  .suggest .button { background: var(--blue); margin-top: 16px; }

  /* Footer */
  .site-footer { height: 435px; background: var(--footer); position: relative; color: var(--footer-text); font-size: 11px; }
  .footer-brand { position: absolute; left: 150px; top: 110px; display: flex; align-items: center; gap: 10px; }
  .footer-brand .brand-name { color: var(--white); }
  .footer-col { position: absolute; top: 80px; }
  .footer-col h4 { font-family: "Montserrat", sans-serif; font-weight: 700; font-size: 13px; color: var(--blue); margin-bottom: 14px; }
  .footer-col li { list-style: none; margin-bottom: 8px; }
  .sitemap { left: 370px; }
  .contact { left: 565px; width: 200px; }
  .contact dt { font-weight: 700; color: var(--white); font-size: 10px; margin-top: 8px; }
  .contact dd { line-height: 1.5; }
  .partners { left: 825px; }
  .partner-badge { width: 200px; height: 46px; background: var(--white); border-radius: 3px; margin-bottom: 14px; }

  .bottom-bar { height: 62px; background: var(--blue); display: flex; justify-content: space-between; align-items: center; padding: 0 120px; font-size: 10px; color: var(--white); }
  .bottom-bar nav { display: flex; gap: 24px; }
</style>
</head>
<body>

<header class="site-header">
  <div class="brand"><span class="brand-mark"></span><span class="brand-name">FERRO WAVE</span></div>
  <div class="account-bar">
    <span>LOGIN &nbsp;|&nbsp; REGISTER</span>
    <span class="search">SEARCH <span>&#9906;</span></span>
  </div>
  <nav class="main-nav">
    <span><span class="key">WHO</span> <span class="rest">WE ARE</span></span>
    <span><span class="key">WHAT</span> <span class="rest">WE DO</span></span>
    <span><span class="key">WHEN</span> <span class="rest">YOU NEED US</span></span>
    <span><span class="key">WHERE</span> <span class="rest">TO REACH US</span></span>
  </nav>
</header>

<section class="hero" role="img" aria-label="Dark city skyline photograph behind the anniversary badge">
  <svg class="hero-badge" width="340" height="380" viewBox="0 0 340 380">
    <polygon points="170,10 320,95 320,285 170,370 20,285 20,95" fill="rgba(15,24,38,.55)" stroke="#ffffff" stroke-width="5"/>
    <rect x="-10" y="128" width="360" height="130" fill="#ffffff" opacity=".08"/>
    <text x="170" y="112" text-anchor="middle" font-family="Montserrat, sans-serif" font-weight="700" font-size="15" fill="#ffffff">CELEBRATED OUR</text>
    <text x="170" y="200" text-anchor="middle" font-family="Montserrat, sans-serif" font-weight="800" font-size="70" fill="#3fa0f0">15 YEARS</text>
    <text x="170" y="232" text-anchor="middle" font-family="Montserrat, sans-serif" font-weight="700" font-size="18" fill="#ffffff" letter-spacing="2">OF HOSTING</text>
    <text x="170" y="278" text-anchor="middle" font-family="Montserrat, sans-serif" font-weight="700" font-size="13" fill="#ffffff">WITHOUT ANY</text>
    <text x="170" y="298" text-anchor="middle" font-family="Montserrat, sans-serif" font-weight="700" font-size="13" fill="#ffffff">DOWNTIME</text>
  </svg>
  <svg class="scroll-cue" width="22" height="34" viewBox="0 0 22 34">
    <rect x="1.5" y="1.5" width="19" height="31" rx="9.5" fill="none" stroke="#ffffff" stroke-width="2"/>
    <line x1="11" y1="8" x2="11" y2="14" stroke="#ffffff" stroke-width="2" stroke-linecap="round"/>
  </svg>
</section>

<section class="welcome">
  <h2 class="section-title">WELCOME TO <span class="accent">FERRO WAVE</span></h2>
  <p>Ferro Wave keeps small company and nonprofit websites online with dependable hosting on a dedicated Linux server. We do not build sites; we give your developer fast FTP access, simple email redirects and friendly support. For fifteen years our partners have helped us keep every site running without downtime, so you can focus on your mission every day.</p>
  <div class="welcome-art" role="img" aria-label="Illustration of connected devices: laptop, monitor, tablet and phone"></div>
</section>

<section class="services">
  <h2 class="section-title"><span class="accent">OUR</span> SERVICES</h2>
  <div class="title-rule"></div>
  <div class="card-row">
    <article class="card">
      <div class="card-art" role="img" aria-label="Web hosting icon"></div>
      <h3 class="card-title">WEB HOSTING</h3>
      <div class="price">$9.99</div>
      <p>Reliable hosting on our dedicated Linux server, per month.</p>
      <span class="button">KNOW MORE</span>
    </article>
    <article class="card">
      <div class="card-art" role="img" aria-label="Domain registration icon"></div>
      <h3 class="card-title">DOMAIN REGISTRATION<br>SERVICES</h3>
      <div class="price">$9.99</div>
      <p>Register a new domain through our trusted partner network.</p>
      <span class="button">KNOW MORE</span>
    </article>
    <article class="card">
      <div class="card-art" role="img" aria-label="Web development icon"></div>
      <h3 class="card-title">WEB DEVELOPMENT<br>SOLUTIONS</h3>
      <div class="price">$9.99</div>
      <p>Referrals to trusted developers for building your new site.</p>
      <span class="button">KNOW MORE</span>
    </article>
  </div>
</section>

<section class="suggest">
  <h2 class="section-title">SUGGEST A <span style="color:var(--blue)">DOMAIN NAME</span></h2>
  <p>Send us a name and we will check it.</p>
  <span class="button">SUBMIT A DOMAIN</span>
</section>

<footer class="site-footer">
  <div class="footer-brand"><span class="brand-mark"></span><span class="brand-name">FERRO WAVE</span></div>
  <div class="footer-col sitemap">
    <h4>SITEMAP</h4>
    <ul>
      <li>Home</li>
      <li>Who We Are</li>
      <li>What We Do</li>
      <li>When You Need Us</li>
      <li>Where To Reach Us</li>
    </ul>
  </div>
  <div class="footer-col contact">
    <h4>CONTACT DETAILS</h4>
    <dl>
      <dt>PHONE &amp; FAX NO.</dt><dd>888.514.2973</dd>
      <dt>EMAIL ADDRESS</dt><dd>myferrowave@mailnest.example</dd>
      <dt>ADDRESS</dt><dd>4819 E. Tolliver Bend #317,<br>Searcy, AR 72143</dd>
    </dl>
  </div>
  <div class="footer-col partners">
    <h4>OUR PARTNERS</h4>
    <div class="partner-badge" role="img" aria-label="Partner badge"></div>
    <div class="partner-badge" role="img" aria-label="Partner badge"></div>
  </div>
</footer>

<div class="bottom-bar">
  <nav><span>Privacy Policy</span><span>Terms of Use</span></nav>
  <span>Copyright 2017 Ferro Wave. All Rights Reserved.</span>
</div>

</body>
</html>
```